Cleaning Business, Premium Services

We need a DL size flyer designs for a cleaning business based in Melbourne, Australia called Bayfield Property Care Cleaning and the slogan is More Time for Life! We would like to keep the corporate colour of blue and red. Our main services are home and office cleaning, window cleaning and carpet cleaning. We are targeting the high net worth clients ie we provide premium services. The final design should communicate quality of service in terms of professionalism and reliability of staff. We would also like a new and creative slogan for the brand. The company's current logo is attached.
Updates

Target Market(s)

High net worth clients, high income clients, corporate executives, clients with big houses and mansions

Industry/Entity Type

Business

Requirements
Must have
• Company's name, corporate colour blue and red | Contact : Darren Whitlow | Mobile: 0412-586-174 | Email: bpc.ashgrove@mailrova.com | A: P O Box 468, Kelmscott Vale VIC 3162
Nice to have
• New slogan. Different corporate colours

```html
<!DOCTYPE html>
<html lang="en">
<head>
<meta charset="utf-8">
<title>Bayfield Property Care Cleaning – DL Flyer</title>
<link href="https://fonts.googleapis.com/css2?family=Josefin+Sans:wght@400&family=Arimo:wght@400;700&display=swap" rel="stylesheet">
<style>
  :root {
    --page-bg: #3b3430;
    --brand-blue: #1a5fb4;
    --bar-blue: #1677d9;
    --brand-red: #e3141b;
    --circle-fill: rgba(68, 70, 76, 0.9);
    --ring-white: #ffffff;
    --photo-light: #e7eaee;
    --photo-mid: #b9c0c8;
    --photo-dark: #3e4247;
  }
  html, body {
    margin: 0;
    width: 1200px;
    height: 1000px;
    overflow: hidden;
    background: var(--page-bg);
  }
  .flyer {
    position: absolute;
    left: 60px;
    top: 239px;
    width: 1080px;
    height: 522px;
    display: block;
  }
  .service-label {
    font-family: "Josefin Sans", sans-serif;
    fill: #ffffff;
    letter-spacing: 1.5px;
    text-anchor: middle;
  }
  .headline {
    font-family: "Josefin Sans", sans-serif;
    fill: #ffffff;
    font-size: 24px;
    letter-spacing: 2px;
    text-anchor: end;
  }
  .brand-name {
    font-family: "Arimo", sans-serif;
    font-weight: 700;
    fill: var(--brand-blue);
  }
  .contact-line {
    font-family: "Arimo", sans-serif;
    font-weight: 700;
    fill: #ffffff;
    font-size: 12px;
  }
  .connector { stroke: #ffffff; stroke-width: 2; opacity: 0.9; }
  .service-ring { fill: var(--circle-fill); stroke: var(--ring-white); stroke-width: 4; }
</style>
</head>
<body>
<svg class="flyer" viewBox="0 0 885 428" xmlns="http://www.w3.org/2000/svg">
  <defs>
    <linearGradient id="interiorTone" x1="0" y1="0" x2="0" y2="1">
      <stop offset="0" stop-color="var(--photo-light)"/>
      <stop offset="0.55" stop-color="var(--photo-mid)"/>
      <stop offset="0.8" stop-color="#d9dde2"/>
      <stop offset="1" stop-color="var(--photo-dark)"/>
    </linearGradient>
    <linearGradient id="redBand" x1="0" y1="0" x2="1" y2="0">
      <stop offset="0" stop-color="var(--brand-red)" stop-opacity="0"/>
      <stop offset="0.18" stop-color="var(--brand-red)"/>
      <stop offset="1" stop-color="var(--brand-red)"/>
    </linearGradient>
    <clipPath id="flyerEdge"><rect width="885" height="428"/></clipPath>
  </defs>

  <g clip-path="url(#flyerEdge)">
    <rect class="interior-photo" width="885" height="428" fill="url(#interiorTone)" role="img" aria-label="Bright modern office lounge with dark sofas, glass tables, potted trees and a city skyline through tall windows"/>

    <!-- headline band -->
    <rect x="460" y="33" width="425" height="47" fill="url(#redBand)"/>
    <text class="headline" x="876" y="65">PROFESSIONAL CLEANING</text>

    <!-- brand panel -->
    <path d="M0 41 H230 A62 62 0 0 1 230 166 H0 Z" fill="#ffffff" opacity="0.55"/>
    <rect x="28" y="86" width="24" height="24" fill="var(--brand-blue)"/>
    <text class="brand-name" x="62" y="98" font-size="26">Bayfield</text>
    <text class="brand-name" x="62" y="120" font-size="15">Property Care</text>

    <!-- connectors -->
    <line class="connector" x1="447" y1="180" x2="678" y2="222"/>
    <line class="connector" x1="213" y1="266" x2="678" y2="232"/>
    <line class="connector" x1="213" y1="282" x2="678" y2="248"/>
    <line class="connector" x1="520" y1="310" x2="682" y2="266"/>

    <!-- service circles -->
    <g class="service windows">
      <circle class="service-ring" cx="375" cy="168" r="73"/>
      <text class="service-label" x="375" y="176" font-size="21">WINDOWS</text>
    </g>
    <g class="service home-office">
      <circle class="service-ring" cx="148" cy="274" r="66"/>
      <text class="service-label" x="148" y="254" font-size="21">HOME</text>
      <text class="service-label" x="148" y="282" font-size="21">AND</text>
      <text class="service-label" x="148" y="310" font-size="21">OFFICE</text>
    </g>
    <g class="service carpets">
      <circle class="service-ring" cx="464" cy="323" r="58"/>
      <text class="service-label" x="464" y="331" font-size="19">CARPETS</text>
    </g>
    <g class="service cleaning">
      <circle class="service-ring" cx="763" cy="240" r="87"/>
      <text class="service-label" x="763" y="250" font-size="27">CLEANING</text>
    </g>
    <g class="service more">
      <circle class="service-ring" cx="836" cy="356" r="48"/>
      <text class="service-label" x="836" y="349" font-size="20">AND</text>
      <text class="service-label" x="836" y="375" font-size="20">MORE</text>
    </g>

    <!-- contact bar -->
    <rect x="0" y="406" width="885" height="22" fill="var(--bar-blue)"/>
    <text class="contact-line" x="7" y="422">CONTACT : DARREN WHITLOW | MOBILE: 0412-586-174 | EMAIL: BPC.ASHGROVE@MAILROVA.COM | A: P O BOX 468, KELMSCOTT VALE VIC 3162</text>
  </g>
</svg>
</body>
</html>
```